Looking for potential sellers

We help people buy and sell homes and are currently looking for potential home sellers. We offer low commissions, are the Local Colorado Springs and Falcon Experts, homes selling fast and at top dollar, Free expert pricing opinions and Consultations, over 9 years of experience, top rated Realtors creative and aggressive marketing strategies. Don't just tour the town, ROAM Kestrelby. phone number 555-013-8842 web roamkestrelby.example

```html
<!DOCTYPE html>
<html lang="en">
<head>
<meta charset="utf-8">
<title>Hearthline Realty Co. – Postcard</title>
<link rel="stylesheet" href="https://fonts.googleapis.com/css2?family=Open+Sans:wght@300;400;600;700;800&display=swap">
<style>
  :root {
    --page-bg: #e4e4e4;
    --taupe: #a49684;
    --taupe-light: #b9ab99;
    --taupe-dark: #7f7264;
    --navy: #1d2630;
    --olive: #9aa23a;
    --olive-bright: #b5bd3e;
    --white: #ffffff;
    --ink: #3a3a3a;
    --rule: #9a9a9a;
  }
  * { box-sizing: border-box; margin: 0; padding: 0; }
  html, body {
    width: 689px; height: 1200px; overflow: hidden;
    background: var(--page-bg);
    font-family: "Open Sans", Arial, sans-serif;
  }
  .postcard {
    position: absolute; left: 24px; width: 640px; height: 426px;
    overflow: hidden; box-shadow: 0 6px 16px rgba(0,0,0,.25);
  }
  .postcard--front { top: 144px; background: linear-gradient(100deg, var(--taupe-light), var(--taupe) 55%, var(--taupe-dark)); }
  .postcard--back { top: 630px; background: var(--white); }

  /* Front */
  .agent-portrait {
    position: absolute; right: 0; top: 0; width: 330px; height: 100%;
    background: radial-gradient(ellipse at 55% 40%, #d9a98a 0%, #c48f72 28%, #8d7766 55%, rgba(127,114,100,0) 80%),
                linear-gradient(180deg, rgba(0,0,0,0) 70%, #3b3f45 100%);
  }
  .front-frame {
    position: absolute; inset: 7px; border: 1px solid rgba(255,255,255,.75); pointer-events: none;
  }
  .brand-mark { position: absolute; left: 34px; top: 68px; color: var(--white); }
  .brand-mark__name { font-size: 24px; font-weight: 600; line-height: 1; }
  .brand-mark__tag { font-size: 6px; font-weight: 600; letter-spacing: .5px; margin-top: 4px; padding-left: 78px; }
  .headline {
    position: absolute; left: 34px; top: 108px; color: var(--white);
    font-size: 42px; font-weight: 800; letter-spacing: -.5px; line-height: 1.1; white-space: nowrap;
  }
  .tagline {
    position: absolute; left: 34px; top: 157px; color: var(--white);
    font-size: 16px; font-weight: 700; line-height: 1.25; white-space: nowrap;
  }
  .offer-band {
    position: absolute; left: 0; top: 204px; width: 100%; height: 172px;
    background: linear-gradient(90deg, var(--navy) 0%, var(--navy) 40%, rgba(29,38,48,.85) 62%, rgba(29,38,48,0) 85%);
  }
  .offer-title {
    position: absolute; left: 34px; top: 209px; color: var(--white);
    font-size: 37px; font-weight: 800; line-height: 1.1; white-space: nowrap;
  }
  .offer-title::after {
    content: ""; position: absolute; left: 0; bottom: -3px; width: 66px; height: 3px; background: var(--olive);
  }
  .offer-list {
    position: absolute; left: 34px; top: 262px; list-style: none;
    color: var(--white); font-size: 11.5px; line-height: 17.8px; white-space: nowrap;
  }
  .offer-list li::before {
    content: ""; display: inline-block; width: 4px; height: 4px; border-radius: 50%;
    background: var(--olive-bright); margin-right: 9px; vertical-align: middle;
  }
  .accent { color: var(--olive-bright); }
  .contact {
    position: absolute; left: 34px; display: flex; align-items: center; color: var(--white); white-space: nowrap;
  }
  .contact__label { position: absolute; left: 0; top: -13px; font-size: 8px; }
  .contact__phone { font-size: 19px; font-weight: 600; display: flex; align-items: center; gap: 4px; }
  .contact__divider { width: 1.5px; height: 22px; background: var(--white); margin: 0 10px; }
  .contact__web { font-size: 11.5px; display: flex; align-items: center; gap: 4px; }
  .postcard--front .contact { top: 391px; }
  .social-dots { display: flex; gap: 4px; }
  .social-dots span { width: 14px; height: 14px; border-radius: 50%; background: var(--white); }
  .postcard--front .social-dots { position: absolute; right: 20px; top: 398px; }

  /* Back */
  .back-shape { position: absolute; inset: 0; }
  .back-scene { position: absolute; left: 0; top: 150px; width: 420px; height: 276px; }
  .back-copy { position: absolute; left: 18px; top: 14px; width: 310px; color: var(--white); }
  .back-copy__kicker { font-size: 21px; font-weight: 300; letter-spacing: .3px; line-height: 1.1; white-space: nowrap; }
  .back-copy__title { font-size: 37px; font-weight: 800; line-height: 1.1; letter-spacing: -.3px; white-space: nowrap; }
  .back-copy__body { font-size: 8.4px; line-height: 12px; margin-top: 6px; }
  .postcard--back .contact { top: 397px; left: 18px; }
  .postcard--back .contact__phone { font-size: 18px; }
  .postcard--back .contact__web { font-size: 10.5px; }
  .postcard--back .social-dots { margin-left: 8px; }
  .return-mark { position: absolute; left: 392px; top: 52px; color: var(--ink); }
  .return-mark__name { font-size: 22px; font-weight: 600; line-height: 1; }
  .return-mark__tag { font-size: 5.5px; font-weight: 600; letter-spacing: .4px; margin-top: 3px; padding-left: 66px; }
  .stamp-box { position: absolute; left: 537px; top: 23px; width: 80px; height: 75px; border: 1px solid var(--rule); }
  .address-line { position: absolute; left: 408px; width: 209px; height: 1px; background: var(--rule); }
</style>
</head>
<body>

<section class="postcard postcard--front" aria-label="Postcard front">
  <div class="agent-portrait" role="img" aria-label="Portrait photograph of the agent on a taupe studio backdrop"></div>
  <div class="brand-mark">
    <div class="brand-mark__name">Hearthline</div>
    <div class="brand-mark__tag">REALTY CO.</div>
  </div>
  <h1 class="headline">It's Time...</h1>
  <p class="tagline">Don't just tour the town,<br>ROAM Kestrelby.</p>
  <div class="offer-band"></div>
  <h2 class="offer-title">WE OFFER</h2>
  <ul class="offer-list">
    <li>Low commissions</li>
    <li>The local colorado springs and falcon experts</li>
    <li>Homes selling fast and at top dollar</li>
    <li><span class="accent">Free</span> expert pricing opinions and consultations</li>
    <li>Over <span class="accent">9 years</span> of experience</li>
    <li>Top rated realtors creative and aggressive marketing strategies</li>
  </ul>
  <div class="contact">
    <span class="contact__label">Get in touch with us</span>
    <span class="contact__phone">
      <svg width="13" height="13" viewBox="0 0 24 24" aria-hidden="true"><path fill="#fff" d="M6.6 10.8a15.1 15.1 0 0 0 6.6 6.6l2.2-2.2c.3-.3.7-.4 1-.2 1.1.4 2.3.6 3.6.6.6 0 1 .4 1 1V20c0 .6-.4 1-1 1A17 17 0 0 1 3 4c0-.6.4-1 1-1h3.5c.6 0 1 .4 1 1 0 1.3.2 2.5.6 3.6.1.3 0 .7-.2 1z"/></svg>
      555-013-8842
    </span>
    <span class="contact__divider"></span>
    <span class="contact__web">
      <svg width="11" height="11" viewBox="0 0 24 24" aria-hidden="true"><g fill="none" stroke="#fff" stroke-width="2"><circle cx="12" cy="12" r="10"/><path d="M2 12h20M12 2c3 3 3 17 0 20M12 2c-3 3-3 17 0 20"/></g></svg>
      roamkestrelby.example
    </span>
  </div>
  <div class="social-dots"><span></span><span></span></div>
  <div class="front-frame"></div>
</section>

<section class="postcard postcard--back" aria-label="Postcard back">
  <svg class="back-shape" width="640" height="426" viewBox="0 0 640 426" aria-hidden="true">
    <defs>
      <linearGradient id="sky-fill" x1="0" y1="0" x2="0" y2="1">
        <stop offset="0" stop-color="#2f5fa8"/>
        <stop offset=".35" stop-color="#4c7fc4"/>
        <stop offset=".6" stop-color="#6f94b8"/>
        <stop offset="1" stop-color="#2b3b52"/>
      </linearGradient>
    </defs>
    <polygon points="0,0 334,0 418,214 398,426 0,426" fill="#9aa23a"/>
    <polygon points="0,0 318,0 404,214 382,426 0,426" fill="url(#sky-fill)"/>
  </svg>
  <div class="back-scene" role="img" aria-label="Photograph of the agent in front of a blue single-storey house with lawn"
       style="background: linear-gradient(180deg, rgba(60,90,120,0) 0%, rgba(50,70,95,.55) 45%, rgba(45,70,45,.7) 75%, rgba(25,30,40,.85) 100%); clip-path: polygon(0 0, 378px 0, 404px 64px, 382px 276px, 0 276px);"></div>
  <div class="back-copy">
    <p class="back-copy__kicker">FIND THE HOME OF</p>
    <h2 class="back-copy__title">YOUR DREAMS</h2>
    <p class="back-copy__body">Whether you're new to the area or a lifelong local, there is no better place to find your ideal home and start truly living your dreams. With sunny days all year and easy access to natural wonders, Kestrelby is an ideal place to put down roots. Ready to start looking for your dream home? Just reach out below!</p>
  </div>
  <div class="contact">
    <span class="contact__label">Get in touch with us</span>
    <span class="contact__phone">
      <svg width="12" height="12" viewBox="0 0 24 24" aria-hidden="true"><path fill="#fff" d="M6.6 10.8a15.1 15.1 0 0 0 6.6 6.6l2.2-2.2c.3-.3.7-.4 1-.2 1.1.4 2.3.6 3.6.6.6 0 1 .4 1 1V20c0 .6-.4 1-1 1A17 17 0 0 1 3 4c0-.6.4-1 1-1h3.5c.6 0 1 .4 1 1 0 1.3.2 2.5.6 3.6.1.3 0 .7-.2 1z"/></svg>
      555-013-8842
    </span>
    <span class="contact__divider"></span>
    <span class="contact__web">
      <svg width="10" height="10" viewBox="0 0 24 24" aria-hidden="true"><g fill="none" stroke="#fff" stroke-width="2"><circle cx="12" cy="12" r="10"/><path d="M2 12h20M12 2c3 3 3 17 0 20M12 2c-3 3-3 17 0 20"/></g></svg>
      roamkestrelby.example
    </span>
    <span class="social-dots"><span></span><span></span></span>
  </div>
  <div class="return-mark">
    <div class="return-mark__name">Hearthline</div>
    <div class="return-mark__tag">REALTY CO.</div>
  </div>
  <div class="stamp-box"></div>
  <div class="address-line" style="top:274px"></div>
  <div class="address-line" style="top:318px"></div>
  <div class="address-line" style="top:361px"></div>
</section>

</body>
</html>
```